Managed Service Provider need new business cards

We are a small Maanged Service Provider of IT Services and need a new fresh design for our business cards. We want something impossible, fun and professional :)
Our services has a large range, but we are always fun and make sure our customers both get their issue sorted and also feel like they are "catching up with an old friend".
All our cards in the past has always been all black, with red and we need something fresher.
The back of card, we would like just a small list of what we do i think, but if someone has a better idea, please do something cool with the back of the card:
Managed IT Services
Productivity Solutions
Data Backup and Recovery
IT System Maintenance
Managed IT Security
More details can be found on our website tqnetworks.com.au
Industry/Entity Type
It Company
Contact Information for Business Card
Name: Dwayne Falstrup
Title: Director
Phone: 03 6193 4827
Mobile: 0412 587 239
Email: dwayne@tqnetworks.com.au
Web: www.tqnetworks.com.au

```html
<!DOCTYPE html>
<html lang="en">
<head>
<meta charset="UTF-8">
<title>TQ Networks — Business Card</title>
<link rel="stylesheet" href="https://fonts.googleapis.com/css2?family=Oswald:wght@700&family=Montserrat:wght@400;500&display=swap">
<style>
  :root {
    --ink: #050505;
    --red: #e8202a;
    --white: #ffffff;
    --stage: #4a4a4c;
  }
  * { margin: 0; padding: 0; box-sizing: border-box; }
  html, body { width: 1200px; height: 965px; overflow: hidden; background: var(--stage); }
  .card {
    position: absolute;
    left: 250px;
    width: 700px;
    height: 400px;
    background: var(--ink);
    overflow: hidden;
    box-shadow: 0 10px 30px rgba(0,0,0,.45);
  }
  .card--back { top: 40px; }
  .card--front { top: 525px; }

  .brand {
    position: absolute;
    left: 0; right: 0;
    text-align: center;
    font-family: "Oswald", sans-serif;
    font-weight: 700;
    font-size: 46px;
    letter-spacing: 2px;
    color: var(--red);
    line-height: 1;
  }
  .card--back .brand { top: 48px; }
  .card--front .brand { top: 108px; }

  .frame-left { position: absolute; left: 0; top: 150px; width: 16px; bottom: 0; background: var(--red); }
  .frame-bottom { position: absolute; left: 0; right: 0; bottom: 0; height: 16px; background: var(--red); }

  .services {
    position: absolute;
    top: 135px; left: 0; right: 0;
    list-style: none;
    text-align: center;
    font-family: "Montserrat", sans-serif;
    font-weight: 500;
    font-size: 17px;
    letter-spacing: 3.5px;
    text-transform: uppercase;
    color: var(--white);
  }
  .services li { padding: 9px 0 8px; position: relative; }
  .services li + li::before {
    content: "";
    position: absolute; top: 0; left: 50%;
    width: 380px; height: 1px; margin-left: -190px;
    background: linear-gradient(90deg, transparent, var(--red), transparent);
  }

  .rule { position: absolute; top: 132px; height: 2px; background: var(--red); }
  .rule--left { left: 0; width: 190px; }
  .rule--right { right: 0; width: 190px; }

  .person { position: absolute; left: 40px; top: 270px; width: 330px; text-align: right; }
  .person__name {
    font-family: "Oswald", sans-serif; font-weight: 700;
    font-size: 38px; letter-spacing: 1px; text-transform: uppercase;
    color: var(--red); line-height: 1.05;
  }
  .person__title { font-family: "Montserrat", sans-serif; font-size: 19px; color: var(--white); }

  .divider { position: absolute; left: 395px; top: 248px; width: 1px; height: 110px; background: var(--white); opacity: .8; }

  .contacts {
    position: absolute; left: 415px; top: 246px;
    list-style: none;
    font-family: "Montserrat", sans-serif; font-size: 16px; color: var(--white);
  }
  .contacts li { display: flex; align-items: center; height: 28px; }
  .contacts svg { width: 16px; height: 16px; margin-right: 12px; flex: none; }
  .accent { color: var(--red); font-weight: 500; }
</style>
</head>
<body>

<section class="card card--back" aria-label="Card back">
  <div class="brand">TQ NETWORKS</div>
  <ul class="services">
    <li>Managed IT Services</li>
    <li>Productivity Solutions</li>
    <li>Data Backup and Recovery</li>
    <li>IT System Maintenance</li>
    <li>Managed IT Security</li>
  </ul>
  <div class="frame-left"></div>
  <div class="frame-bottom"></div>
</section>

<section class="card card--front" aria-label="Card front">
  <div class="rule rule--left"></div>
  <div class="brand">TQ NETWORKS</div>
  <div class="rule rule--right"></div>

  <div class="person">
    <div class="person__name">Dwayne Falstrup</div>
    <div class="person__title">Director</div>
  </div>

  <div class="divider"></div>

  <ul class="contacts">
    <li>
      <svg viewBox="0 0 16 16" fill="none" stroke="#e8202a" stroke-width="1.4"><path d="M4 2l2.5 3-1.5 1.5a8 8 0 0 0 4.5 4.5L11 9.5l3 2.5-1.5 2C7 14 2 9 2 3.5z"/></svg>
      03 6193 4827
    </li>
    <li>
      <svg viewBox="0 0 16 16" fill="none" stroke="#e8202a" stroke-width="1.4"><rect x="4.5" y="1.5" width="7" height="13" rx="1.2"/><line x1="7" y1="12.5" x2="9" y2="12.5"/></svg>
      0412 587 239
    </li>
    <li>
      <svg viewBox="0 0 16 16" fill="none" stroke="#e8202a" stroke-width="1.4"><rect x="1.5" y="3.5" width="13" height="9"/><path d="M1.5 3.5L8 9l6.5-5.5"/></svg>
      dwayne@tqnetworks.com.au
    </li>
    <li>
      <svg viewBox="0 0 16 16" fill="none" stroke="#e8202a" stroke-width="1.4"><circle cx="8" cy="8" r="6.5"/><ellipse cx="8" cy="8" rx="2.8" ry="6.5"/><line x1="1.5" y1="8" x2="14.5" y2="8"/></svg>
      <span>www.<span class="accent">tqnetworks</span>.com.au</span>
    </li>
  </ul>
</section>

</body>
</html>
```